Education portal needs a new Email Creative Design

We could not decide on the creative earlier as we were unable to picture how will it look. Hence, we have added content so that we can choose the best design of all. Below is the content to be used for the email creative:
____________________________________
Did you know that 25% of all Americans have experienced at least one divorce?*
41% of first marriages end in divorce!!*

Over 1 million children are affected by divorce each year*

Become a Marriage and Family therapist - Achieve inner-happiness by helping individuals, families and couples resolve their struggles and enhance their lives.
Family Therapists are trained in various modes of therapy in order to prepare them for work with individuals, families, couples, and groups.

With proper training, you will be able to treat:
• Depression and other Affective Disorders
• Childhood Behavioral and Emotional Disorders
• Marital and Relationship Problems
• Conduct Disorder and Delinquency
• Substance Abuse
• Alcoholism
• Domestic Violence
• Severe Mental Illness
• Physical Illness

You could also qualify for financial aid* from the government to pursue this career..

Secure your life by earning upto $78,580* and attain peace of mind while helping others..

__________________________

These are the links to images we liked, but if you have something better, we would love to see them:
http://www.pexalunto.com/photo/seperated-58301947?st=7bk2913
http://www.pexalunto.com/photo/domestic-violence-72950386?st=f84m615

We are an education portal offering options of schools, colleges, universities and courses to students and working professionals.

We are looking for an email creative which has great call-to-action; be creative and research more if you wish.
Incorporate call-to-action tabs, make it colorful, include pictures and content.
Also attached are industry standard creatives for your reference, let me know if you have any questions.

Please see new files uploaded

I have uploaded a new creative made by our design team. Follow similar guidelines

For those who have not submitted their designs, please send us soon. Thanks

We thought a content brief will do more justice to this design contest hence we have updated our brief with new content to create a newer design Please submit your designs soon. Thanks

Target Market(s)

25 to 50 years working professionals

Industry/Entity Type

Government

Font styles to use
Serif
Sans Serif
Decorative
Script

Requirements
Must have
• Call-to-action

```html
<!DOCTYPE html>
<html lang="en">
<head>
<meta charset="utf-8">
<title>Become a Marriage and Family Therapist</title>
<link href="https://fonts.googleapis.com/css2?family=Oswald:wght@500;600&family=Source+Sans+3:wght@400;600;700&display=swap" rel="stylesheet">
<style>
  :root {
    --sky: #a8dcea;
    --sky-deep: #9fd6e6;
    --ink: #56595c;
    --lime: #cbdc2c;
    --red: #c8102e;
    --dark: #232325;
    --dark-mid: #3c3d40;
    --white: #ffffff;
    --frame: #a9dff0;
  }
  * { box-sizing: border-box; margin: 0; padding: 0; }
  html, body { width: 837px; height: 1200px; overflow: hidden; background: var(--white); }
  .email { position: relative; width: 837px; height: 1200px; font-family: "Source Sans 3", Arial, sans-serif; color: var(--ink); }

  .top-band { position: absolute; left: 0; top: 0; width: 837px; height: 60px; background: var(--sky); }
  .logo-box { position: absolute; left: 362px; top: 11px; width: 113px; height: 38px; border: 2px solid #6d7377; display: flex; align-items: center; justify-content: center; font-size: 20px; letter-spacing: 1px; color: #555; }

  .stats-header { position: absolute; left: 0; top: 74px; width: 837px; height: 172px; background: linear-gradient(180deg, #2e2f31 0%, var(--dark) 60%, #2a2b2d 100%); font-family: "Oswald", Impact, sans-serif; color: var(--white); }
  .stats-header .ask { position: absolute; left: 30px; top: 20px; width: 125px; text-align: center; font-size: 36px; line-height: 40px; font-weight: 600; text-transform: uppercase; }
  .stat { position: absolute; display: flex; align-items: flex-start; white-space: nowrap; }
  .stat .num { color: var(--lime); font-size: 52px; line-height: 52px; font-weight: 600; }
  .stat .num sup { font-size: 24px; vertical-align: top; line-height: 30px; }
  .stat .txt { margin-left: 6px; font-size: 29px; line-height: 31px; font-weight: 500; text-transform: uppercase; }
  .stat-one { left: 160px; top: 18px; }
  .stat-two { left: 168px; top: 96px; }

  .hero { position: absolute; left: 0; top: 246px; width: 837px; height: 445px; background: linear-gradient(180deg, #5a5b5e 0%, var(--dark-mid) 55%, #1f2022 100%); }
  .hero-photo { position: absolute; left: 27px; top: 17px; width: 640px; height: 388px; border: 3px solid var(--frame); border-radius: 10px; background: linear-gradient(90deg, #3f6f86 0%, #5f8fa3 30%, #6e94a6 48%, #8a6a4f 52%, #b8906a 75%, #6e5238 100%); }
  .hero-callout { position: absolute; left: 670px; top: 14px; width: 164px; text-align: center; font-family: "Oswald", Impact, sans-serif; color: var(--white); text-transform: uppercase; font-weight: 500; white-space: nowrap; }
  .hero-callout .lead { font-size: 27px; line-height: 33px; }
  .hero-callout .big { color: var(--lime); font-size: 38px; line-height: 46px; margin-top: 4px; font-weight: 600; }
  .hero-callout .tail { font-size: 25px; line-height: 33px; margin-top: 4px; }
  .btn { position: absolute; display: flex; align-items: center; justify-content: center; background: var(--red); color: var(--white); font-family: "Oswald", Impact, sans-serif; font-weight: 500; text-transform: uppercase; text-decoration: none; }
  .btn-learn { left: 606px; top: 379px; width: 214px; height: 46px; font-size: 23px; }

  .content { position: absolute; left: 0; top: 691px; width: 837px; height: 337px; }
  .col-left { position: absolute; left: 34px; top: 22px; width: 380px; font-size: 19px; line-height: 27px; white-space: nowrap; }
  .col-left p + p { margin-top: 27px; }
  .col-left strong { font-weight: 700; color: #4a4d50; }
  .col-right { position: absolute; left: 421px; top: 22px; width: 410px; font-size: 19px; line-height: 27px; white-space: nowrap; }
  .treat-list { list-style: none; margin-left: 10px; }
  .treat-list li { position: relative; padding-left: 11px; }
  .treat-list li::before { content: ""; position: absolute; left: 0; top: 11px; width: 7px; height: 7px; border-radius: 50%; background: var(--red); }

  .aid-band { position: absolute; left: 0; top: 1028px; width: 837px; height: 111px; background: var(--sky-deep); padding: 17px 0 0 34px; font-size: 19px; line-height: 27px; }
  .aid-band p + p { margin-top: 19px; }
  .aid-band strong { font-weight: 700; color: #4a4d50; }

  .btn-cta { left: 267px; top: 1153px; width: 302px; height: 45px; font-size: 22px; }
</style>
</head>
<body>
<div class="email">
  <header class="top-band">
    <div class="logo-box">LOGO</div>
  </header>

  <section class="stats-header">
    <div class="ask">Did you know that</div>
    <div class="stat stat-one"><span class="num">25<sup>%</sup></span><span class="txt">of all Americans have experienced<br>at least one divorce?</span></div>
    <div class="stat stat-two"><span class="num">41<sup>%</sup></span><span class="txt">of first marriages<br>end in divorce?</span></div>
  </section>

  <section class="hero">
    <div class="hero-photo" role="img" aria-label="Photo behind cracked glass: a couple arguing on the left, a tearful young girl on the right"></div>
    <div class="hero-callout">
      <div class="lead">Did you<br>know<br>that</div>
      <div class="big">Over<br>1 million<br>children</div>
      <div class="tail">are affected<br>by divorce<br>each year?</div>
    </div>
    <a class="btn btn-learn" href="#">Learn more</a>
  </section>

  <section class="content">
    <div class="col-left">
      <p>Become a <strong>Marriage and Family therapist</strong><br>-Achieve inner-happiness by helping<br>individuals, families and couples resolve<br>their struggles and enhance their lives.</p>
      <p><strong>Family Therapists</strong> are trained in various<br>modes of therapy in order to prepare them<br>for work with individuals, families, couples,<br>and groups.</p>
    </div>
    <div class="col-right">
      <p>With proper training, you will be<br>able to treat:</p>
      <ul class="treat-list">
        <li>Depression and other Affective Disorders</li>
        <li>Childhood Behavioral and Emotional Disorders</li>
        <li>Marital and Relationship Problems</li>
        <li>Conduct Disorder and Delinquency</li>
        <li>Substance Abuse</li>
        <li>Alcoholism</li>
        <li>Domestic Violence</li>
        <li>Severe Mental Illness</li>
        <li>Physical Illness</li>
      </ul>
    </div>
  </section>

  <section class="aid-band">
    <p>You could also qualify for <strong>financial aid*</strong> from the government to pursue this career.</p>
    <p>Secure your life by earning upto <strong>$78,580*</strong> and attain peace of mind while helping others.</p>
  </section>

  <a class="btn btn-cta" href="#">Become a therapist now!</a>
</div>
</body>
</html>
```